Menu Design for Indian Restaurant

We are a new Indian restaurant, named Saffron Lantern Restaurant, looking for a sophisticated looking menu. It is a semi-formal dining restaurant with wooden tables and chairs and will have a focus on a creating a lively atmosphere. Environment-friendly products will be used, and the menu will be 100% vegetarian. There will be an emphasis on fresh, healthy and delicious food. We will be targeting vegans, vegetarians, health conscious people, people from all age groups, Indians, Australian's as well as other ethnic communities. We need a clean, simple, sophisticated design for the new restaurant menu. Attached is the restaurant logo for reference.

UPDATE:
- We have attached the menu
- We are not looking for any particular type of layout or size (open to suggests). Please suggest this after having a look at the menu contents. However, we will be having one formal menu to be used in the restaurant, and one in brochure form for distribution.
- There are no images at present. If you feel the need of images, please use sample images for now.

Thank you for the entries thus far.
Updates

Target Market(s)

All age groups from different nationalities

Industry/Entity Type

Indian Restaurant

Colors

Designer to choose colors to be used in the design.

Requirements
Nice to have
• This will be printed on environmentally friendly paper.

```html
<!DOCTYPE html>
<html lang="en">
<head>
<meta charset="utf-8">
<title>Saffron Lantern Restaurant – Menu</title>
<link rel="stylesheet" href="https://fonts.googleapis.com/css2?family=Dancing+Script:wght@700&family=Open+Sans:wght@400;700&display=swap">
<style>
  :root {
    --paper: #ffffff;
    --charcoal: #3b3c3d;
    --ink: #2b2b2b;
    --muted: #7a7a7a;
    --chili: #c8222a;
    --leaf: #8cc63f;
    --pale: #e6e6e6;
  }
  html, body { margin: 0; padding: 0; overflow: hidden; }
  body { width: 849px; height: 1200px; background: var(--paper); font-family: "Open Sans", sans-serif; position: relative; }
  .menu { position: absolute; inset: 0; overflow: hidden; }

  .brand { position: absolute; left: 0; top: 0; width: 330px; height: 98px; display: flex; flex-direction: column; align-items: center; justify-content: center; color: var(--charcoal); font-weight: 700; }
  .brand .name { font-size: 26px; letter-spacing: 1px; line-height: 1; }
  .brand .sub { font-size: 10px; letter-spacing: 4px; margin-top: 6px; }

  .photo-entree { position: absolute; left: 18px; top: 102px; width: 304px; height: 112px; background: linear-gradient(135deg, #7a4a2a, #c98a4a 45%, #e9d7b8 70%, #5c6b3a); }
  .photo-mains { position: absolute; left: 330px; top: 0; width: 519px; height: 105px; background: linear-gradient(90deg, #9aa07a, #6d7a4a 40%, #c9b58a 75%, #4f4a3a); }

  .entree-panel { position: absolute; left: 0; top: 226px; width: 330px; bottom: 0; background: var(--charcoal); }
  .entree-panel h2 { margin: 0; position: absolute; left: 18px; top: 28px; font-family: "Dancing Script", cursive; color: var(--chili); font-size: 38px; font-weight: 700; }
  .entree-list { position: absolute; left: 18px; top: 160px; width: 300px; margin: 0; padding: 0; list-style: none; }
  .entree-list li { height: 42px; }
  .entree-list .dish { color: var(--leaf); font-size: 11px; font-weight: 700; display: block; }
  .entree-list .desc { color: var(--pale); font-size: 9px; display: block; margin-top: 2px; }

  .mains { position: absolute; left: 345px; top: 105px; right: 40px; bottom: 0; }
  .mains h2 { margin: 0; position: absolute; right: 0; top: 8px; font-family: "Dancing Script", cursive; color: var(--chili); font-size: 32px; font-weight: 700; }
  .mains-list { position: absolute; left: 25px; top: 62px; margin: 0; padding: 0; list-style: none; width: 420px; }
  .mains-list li { height: 50.5px; }
  .mains-list .dish { color: var(--ink); font-size: 12px; font-weight: 700; display: block; }
  .mains-list .desc { color: var(--muted); font-size: 9px; display: block; margin-top: 2px; }
</style>
</head>
<body>
<div class="menu">
  <div class="brand">
    <span class="name">Saffron Lantern</span>
    <span class="sub">RESTAURANT</span>
  </div>

  <div class="photo-entree" role="img" aria-label="Photo of grilled tandoori starters on a plate"></div>
  <div class="photo-mains" role="img" aria-label="Photo of fresh vegetarian dishes on a table"></div>

  <section class="entree-panel">
    <h2>Entree (Tapas)</h2>
    <ul class="entree-list">
      <li><span class="dish">KAMAL KOFTA (4PCS) 6.9</span><span class="desc">Crispy lotus stem balls in rich onion gravy</span></li>
      <li><span class="dish">HARA KEBAB (4PCS) 6.9</span><span class="desc">Spinach and pea patties, grilled in tandoor</span></li>
      <li><span class="dish">TANDOORI FOOL (3PCS) 6.9</span><span class="desc">Cauliflower marinated in spiced yoghurt, charred</span></li>
      <li><span class="dish">TANDOORI MUSHROOMS (4PCS) 7.9</span><span class="desc">Button mushrooms with mint and chilli</span></li>
      <li><span class="dish">MOMOS (6) 6.9</span><span class="desc">Steamed dumplings filled with fresh vegetables</span></li>
      <li><span class="dish">TANDOORI MOMOS (6) 7.9</span><span class="desc">Momos roasted in tandoor with spices</span></li>
      <li><span class="dish">MUSHROOMS MOMOS (6) 6.9</span><span class="desc">Dumplings stuffed with garlic mushrooms</span></li>
      <li><span class="dish">PANEER TIKKA (4PCS) 7.9</span><span class="desc">Cottage cheese cubes from the clay oven</span></li>
      <li><span class="dish">KABULI TIKI (4PCS) 6.9</span><span class="desc">Chickpea patties with mint and tamarind</span></li>
      <li><span class="dish">SAMOSA CHAT (2PCS) 6.9</span><span class="desc">Crushed samosa with chutneys and yoghurt</span></li>
      <li><span class="dish">ALOO TIKKI CHAT (2PCS) 6.9</span><span class="desc">Potato patties topped with chickpea curry</span></li>
      <li><span class="dish">DHAI BHALLA PAPRI 6.9</span><span class="desc">Lentil dumplings, crisp wafers and yoghurt</span></li>
    </ul>
  </section>

  <section class="mains">
    <h2>Taste of North East</h2>
    <ul class="mains-list">
      <li><span class="dish">Chilli Honey Dry 6.9</span><span class="desc">Crispy cauliflower tossed in honey chilli</span></li>
      <li><span class="dish">Chilli Tofu Dry 6.9</span><span class="desc">Tofu with peppers, onion and soy</span></li>
      <li><span class="dish">Vegetable Spring Roll (3pcs) 6.9</span><span class="desc">Vegetable filled rolls with sweet chilli</span></li>
      <li><span class="dish">Chilli Mushrooms Dry (4pcs) 7.9</span><span class="desc">Mushrooms tossed with garlic and capsicum</span></li>
      <li><span class="dish">Chilli Soya Paneer Dry 10.9</span><span class="desc">Soya and paneer in tangy chilli sauce</span></li>
      <li><span class="dish">Burger Pakode</span><span class="desc">Spiced potato patty in soft bun</span></li>
      <li><span class="dish">Grass Hopper 7.9</span><span class="desc">Fresh mint and pistachio cooler</span></li>
      <li><span class="dish">Cheese Hopper 7.9</span><span class="desc">Creamy cheese and herb cooler</span></li>
      <li><span class="dish">Dakshani Dhum</span><span class="desc">Smoky south Indian style platter</span></li>
      <li><span class="dish">Rava Dosa 10.9</span><span class="desc">Thin semolina crepe with chutneys</span></li>
      <li><span class="dish">Onion Rava Dosa 11.9</span><span class="desc">Semolina crepe with crisp onions</span></li>
      <li><span class="dish">Plain Dosa 10.9</span><span class="desc">Crisp rice crepe with sambar</span></li>
      <li><span class="dish">Udupi Masala Dosa 11.9</span><span class="desc">Rice crepe filled with spiced potato</span></li>
      <li><span class="dish">Paneer Dosa 12.9</span><span class="desc">Crepe filled with grated paneer masala</span></li>
      <li><span class="dish">Vada sambar (2pcs) 6.9</span><span class="desc">Lentil doughnuts in hot sambar</span></li>
      <li><span class="dish">Thair Vada 6.9</span><span class="desc">Lentil doughnuts in chilled yoghurt</span></li>
      <li><span class="dish">Dhai Idly 6.9</span><span class="desc">Steamed rice cakes in yoghurt</span></li>
      <li><span class="dish">Idly (3pcs) One each 6.9</span><span class="desc">Soft steamed rice cakes with sambar</span></li>
      <li><span class="dish">VADA AND IDLY PLATE 6.9</span><span class="desc">Vada and idly with chutneys</span></li>
      <li><span class="dish">CHANNA BHTURA (2pcs) 9.9</span><span class="desc">Chickpea curry with fried bread</span></li>
    </ul>
  </section>
</div>
</body>
</html>
```